Postcard Design

I am a mortgage broker located in Michigan. I recently opened my own company after working for another for 7 years. I want to send out a mailing letting my old clients know my new information and also reach out to them to let me know if I can assist them with anything.

Industry/Entity Type

It Company

```html
<!DOCTYPE html>
<html lang="en">
<head>
<meta charset="utf-8">
<title>Lakeport Lending Postcard</title>
<link rel="stylesheet" href="https://fonts.googleapis.com/css2?family=Roboto+Condensed:wght@400;700;800&family=Open+Sans:wght@400;600&display=swap">
<style>
  :root {
    --blue: #1f5f9c;
    --blue-deep: #164a7c;
    --ink: #111417;
    --slate: #3b4046;
    --paper: #ffffff;
    --backdrop: #ece9e4;
    --rule: #c9cdd1;
  }
  * { box-sizing: border-box; margin: 0; padding: 0; }
  html, body { width: 907px; height: 1200px; overflow: hidden; }
  body { background: var(--backdrop); position: relative; font-family: "Open Sans", sans-serif; }

  .card { position: absolute; left: 113px; width: 699px; height: 541px; background: var(--paper); overflow: hidden; box-shadow: 0 2px 8px rgba(0,0,0,.18); }
  .card--front { top: 36px; }
  .card--back { top: 602px; height: 540px; }
  .card svg.art { position: absolute; left: 0; top: 0; }

  .brand { position: absolute; display: flex; align-items: center; gap: 7px; font-family: "Roboto Condensed", sans-serif; font-weight: 700; color: var(--blue); white-space: nowrap; }
  .brand__mark { width: 14px; height: 14px; background: var(--blue); }
  .card--front .brand { left: 30px; top: 78px; font-size: 17px; }
  .card--back .brand { left: 22px; top: 84px; font-size: 14px; }

  .headline { position: absolute; left: 232px; top: 22px; font-family: "Roboto Condensed", sans-serif; font-weight: 800; }
  .headline__num { position: absolute; left: 0; top: -4px; font-size: 158px; line-height: 1; color: var(--blue); letter-spacing: -6px; }
  .headline__years { position: absolute; left: 102px; top: 10px; font-size: 60px; line-height: 1; color: var(--blue); }
  .headline__exp { position: absolute; left: 100px; top: 64px; font-size: 62px; line-height: 1; color: var(--ink); white-space: nowrap; }

  .pitch { position: absolute; left: 433px; top: 250px; font-family: "Roboto Condensed", sans-serif; font-weight: 700; line-height: 1; white-space: nowrap; }
  .pitch__role { font-size: 33px; color: var(--ink); }
  .pitch__cta { font-size: 37px; color: var(--blue); margin-top: 6px; }
  .pitch__phone { font-size: 38px; color: var(--ink); margin-top: 8px; letter-spacing: .5px; }

  .visit { position: absolute; left: 463px; top: 458px; width: 210px; text-align: center; color: #fff; }
  .visit__label { font-family: "Roboto Condensed", sans-serif; font-weight: 700; font-size: 19px; }
  .visit__url { font-size: 17px; margin-top: 4px; }

  .intro { position: absolute; left: 24px; top: 188px; width: 288px; color: #fff; font-size: 12.5px; line-height: 18px; text-align: justify; hyphens: auto; }
  .contact { position: absolute; left: 24px; top: 328px; color: #fff; }
  .contact__title { font-family: "Roboto Condensed", sans-serif; font-weight: 700; font-size: 21px; margin-bottom: 8px; }
  .contact__row { display: flex; align-items: center; gap: 5px; font-size: 14.5px; line-height: 20px; }
  .contact__row svg { flex: none; }

  .stamp { position: absolute; left: 600px; top: 16px; width: 80px; height: 86px; background: #bdbdbd; }
  .address-line { position: absolute; left: 424px; width: 176px; height: 2px; background: var(--rule); }
</style>
</head>
<body>

<section class="card card--front">
  <svg class="art" width="699" height="541" viewBox="0 0 699 541">
    <defs>
      <linearGradient id="frontPhoto" x1="0" y1="0" x2="0.6" y2="1">
        <stop offset="0" stop-color="#c3c9d0"/>
        <stop offset="0.5" stop-color="#dde5ea"/>
        <stop offset="1" stop-color="#e6f2f3"/>
      </linearGradient>
      <radialGradient id="panelGlow" cx="0.5" cy="0.5" r="0.6">
        <stop offset="0" stop-color="#ffffff"/>
        <stop offset="1" stop-color="#e4e6e8"/>
      </radialGradient>
      <linearGradient id="portraitFront" x1="0" y1="0" x2="0" y2="1">
        <stop offset="0" stop-color="#f4f4f4"/>
        <stop offset="0.6" stop-color="#e2e4e6"/>
        <stop offset="1" stop-color="#6b7888"/>
      </linearGradient>
    </defs>
    <ellipse cx="540" cy="315" rx="230" ry="130" fill="url(#panelGlow)"/>
    <path d="M330,205 C440,160 615,165 699,262" fill="none" stroke="var(--slate)" stroke-width="12"/>
    <path d="M322,196 C440,150 620,155 699,248" fill="none" stroke="var(--blue)" stroke-width="7"/>
    <path d="M420,541 L420,468 C500,440 610,430 699,398 L699,541 Z" fill="var(--slate)"/>
    <path d="M420,462 C500,436 610,424 699,390" fill="none" stroke="var(--blue)" stroke-width="5"/>
    <g role="img" aria-label="Photo of a business meeting with a small model house on a glass desk">
      <path d="M0,124 C150,110 300,140 352,212 C395,275 412,400 424,541 L0,541 Z" fill="url(#frontPhoto)"/>
    </g>
    <path d="M0,118 C150,104 306,134 359,208 C402,272 419,400 431,541" fill="none" stroke="var(--blue)" stroke-width="7"/>
    <circle cx="387" cy="442" r="80" fill="#fff" stroke="var(--blue)" stroke-width="4"/>
    <g role="img" aria-label="Portrait of the mortgage broker">
      <circle cx="387" cy="442" r="70" fill="url(#portraitFront)"/>
    </g>
  </svg>

  <div class="brand"><span class="brand__mark"></span>LAKEPORT LENDING</div>

  <h1 class="headline">
    <span class="headline__num">7</span>
    <span class="headline__years">YEARS</span>
    <span class="headline__exp">EXPERIENCE</span>
  </h1>

  <div class="pitch">
    <p class="pitch__role">MortgageBroker</p>
    <p class="pitch__cta">Contact now</p>
    <p class="pitch__phone">0123456789</p>
  </div>

  <div class="visit">
    <p class="visit__label">Visit us</p>
    <p class="visit__url">www.yourcompany.com</p>
  </div>
</section>

<section class="card card--back">
  <svg class="art" width="699" height="540" viewBox="0 0 699 540">
    <defs>
      <linearGradient id="backPhoto" x1="0" y1="0" x2="1" y2="0">
        <stop offset="0" stop-color="#ffffff"/>
        <stop offset="0.3" stop-color="#edf1f4"/>
        <stop offset="1" stop-color="#d6dee5"/>
      </linearGradient>
      <linearGradient id="blueBand" x1="0" y1="0" x2="1" y2="0">
        <stop offset="0" stop-color="var(--blue-deep)"/>
        <stop offset="1" stop-color="var(--blue)"/>
      </linearGradient>
      <linearGradient id="portraitBack" x1="0" y1="0" x2="0" y2="1">
        <stop offset="0" stop-color="#f4f4f4"/>
        <stop offset="0.6" stop-color="#e2e4e6"/>
        <stop offset="1" stop-color="#6b7888"/>
      </linearGradient>
    </defs>
    <g role="img" aria-label="Photo of house keys on a mortgage loan form being signed">
      <path d="M90,0 L362,0 C370,50 368,110 360,162 L90,162 Z" fill="url(#backPhoto)"/>
    </g>
    <path d="M0,162 L360,162 C356,210 350,260 340,300 C240,290 120,290 0,300 Z" fill="url(#blueBand)"/>
    <path d="M0,300 C120,290 240,290 340,300 C320,360 290,420 262,445 L0,445 Z" fill="var(--slate)"/>
    <path d="M366,0 C378,110 366,220 338,302" fill="none" stroke="var(--slate)" stroke-width="5"/>
    <circle cx="324" cy="383" r="80" fill="#fff" stroke="var(--blue)" stroke-width="4"/>
    <g role="img" aria-label="Portrait of the mortgage broker">
      <circle cx="324" cy="383" r="70" fill="url(#portraitBack)"/>
    </g>
  </svg>

  <div class="brand"><span class="brand__mark"></span>LAKEPORT LENDING</div>

  <p class="intro" lang="la">Lorem ipsum dolor sit amet, mea ei doming necessitatibus, in iudico prompta vocibus est, ei nonumes postulant repudiandae eam. Pro te vidit euismod reprehendunt, nam ocurreret splendide suscipiantur te. Ea quo legere eruditi interesset,aliberavisse mei at.</p>

  <div class="contact">
    <h2 class="contact__title">Contact</h2>
    <p class="contact__row">
      <svg width="13" height="13" viewBox="0 0 24 24"><circle cx="12" cy="12" r="10" fill="none" stroke="#fff" stroke-width="2"/><path d="M9 7c-1 1-1 3 1 6s4 4 5 3l1-1-2-2-1 1c-1 0-3-2-3-3l1-1-2-3z" fill="#fff"/></svg>
      0123456789
    </p>
    <p class="contact__row">
      <svg width="13" height="13" viewBox="0 0 24 24"><rect x="2" y="5" width="20" height="14" fill="#fff"/><path d="M2 5l10 8 10-8" fill="none" stroke="var(--slate)" stroke-width="2"/></svg>
      www.yourcompny@mail.com
    </p>
    <p class="contact__row">
      <svg width="13" height="13" viewBox="0 0 24 24"><circle cx="12" cy="12" r="9" fill="none" stroke="#fff" stroke-width="2"/><path d="M3 12h18M12 3c4 4 4 14 0 18M12 3c-4 4-4 14 0 18" fill="none" stroke="#fff" stroke-width="1.5"/></svg>
      www.yourcompany.com
    </p>
  </div>

  <div class="stamp"></div>
  <div class="address-line" style="top:213px"></div>
  <div class="address-line" style="top:255px"></div>
  <div class="address-line" style="top:299px"></div>
</section>

</body>
</html>
```